International Perfume distribution Company needs a stationary design

We are a perfume development and distribution company named MORVA and based in Sao Paulo Brazil. Basically we licence brazilian and international brands and celebrities to develop and distribute its fragrances and perfumes in Brazil. Our current licenced brands are: Kelp Orbita, Verdun, Lodge Fimbra fragrances and Lara Quintelo (brazilian soap opera celebrity).

We already have our logo and brand that reflects our massive distribution power in Brazil ("spraying our products accross Brazil") and we are also a branch of a big distribution company named DRAVEN. It would be nice to mention it in our stationary ("uma divisao do grupo Draven").

Industry/Entity Type

It Company

Requirements
Must have
• mention that Morva is a division/branch of draven using the following phrase: "uma divisão do grupo Draven"

Use the logo signature: international fragrances

```html
<!DOCTYPE html>
<html lang="pt">
<head>
<meta charset="utf-8">
<title>Morva — Stationery</title>
<link href="https://fonts.googleapis.com/css2?family=Josefin+Sans:wght@300;400;600;700&display=swap" rel="stylesheet">
<style>
  :root {
    --violet: #3b2f8a;
    --amber: #f2a530;
    --paper: #ffffff;
    --stage: #ffffff;
    --ink-soft: #6a6a72;
    --line: #e4e4ea;
  }
  * { margin: 0; padding: 0; box-sizing: border-box; }
  html, body { width: 1200px; height: 1000px; overflow: hidden; }
  body {
    background: var(--stage);
    font-family: "Josefin Sans", sans-serif;
    position: relative;
  }

  /* shared brand mark: plain circle + name */
  .brand { position: absolute; display: flex; align-items: center; }
  .brand__dot { border-radius: 50%; background: var(--amber); flex: none; }
  .brand__name { color: var(--violet); font-weight: 300; line-height: 1; }

  .rule { position: absolute; }
  .rule__violet { display: block; background: var(--violet); }
  .rule__amber { display: block; background: var(--amber); }

  /* business card — front */
  .card {
    position: absolute;
    width: 230px; height: 131px;
    top: 51px;
    border: 1px solid var(--line);
  }
  .card--front { left: 326px; background: var(--paper); }
  .card--front .brand { left: 12px; top: 16px; gap: 8px; }
  .card--front .brand__dot { width: 22px; height: 22px; }
  .card--front .brand__name { font-size: 19px; }
  .card__person { position: absolute; right: 8px; top: 37px; text-align: right; }
  .card__name { font-size: 8px; font-weight: 700; color: var(--violet); }
  .card__role { font-size: 7.5px; color: var(--ink-soft); margin-top: 2px; }
  .card--front .rule { left: 0; right: 0; top: 59px; }
  .card--front .rule__violet { height: 6px; }
  .card--front .rule__amber { height: 3px; }
  .card__contact {
    position: absolute; left: 14px; top: 81px;
    font-size: 8px; color: var(--ink-soft); line-height: 12px;
  }
  .card__contact .sep { color: #222; margin: 0 3px; font-weight: 600; }

  /* business card — back */
  .card--back {
    left: 607px; background: var(--violet); border: none;
    display: flex; align-items: center; justify-content: center;
  }
  .card__url {
    color: #fff; font-size: 13px; font-weight: 700; letter-spacing: 2.5px;
  }

  /* letterhead */
  .letterhead {
    position: absolute; left: 301px; top: 220px;
    width: 561px; height: 725px;
    background: var(--paper);
    border: 1px solid var(--line);
  }
  .letterhead .brand { left: 26px; top: 36px; gap: 24px; }
  .letterhead .brand__dot { width: 64px; height: 64px; }
  .letterhead .brand__name { font-size: 42px; }
  .letterhead__affiliation {
    position: absolute; right: 6px; top: 78px;
    color: var(--amber); font-size: 9.5px; font-weight: 700;
    letter-spacing: 2.2px; text-transform: uppercase;
  }
  .letterhead .rule { left: 247px; right: 0; top: 91px; }
  .letterhead .rule__violet { height: 6px; }
  .letterhead .rule__amber { height: 3px; }
  .letterhead__footer {
    position: absolute; left: 0; right: 0; bottom: 0; height: 35px;
    background: var(--violet); color: #fff;
    display: flex; align-items: center; justify-content: center;
    font-size: 10px; letter-spacing: 1.5px; padding-top: 2px;
  }
  .letterhead__footer .phone { font-size: 12.5px; font-weight: 600; letter-spacing: 1px; }
  .letterhead__footer .site b { font-size: 12px; font-weight: 600; }
  .letterhead__footer .sep { margin: 0 5px; }
</style>
</head>
<body>

  <section class="card card--front" aria-label="Business card front">
    <div class="brand">
      <span class="brand__dot"></span>
      <span class="brand__name">MORVA</span>
    </div>
    <div class="card__person">
      <p class="card__name">Tomas Reval</p>
      <p class="card__role">Founder</p>
    </div>
    <div class="rule"><span class="rule__violet"></span><span class="rule__amber"></span></div>
    <div class="card__contact">
      <p>P: 555.210.4471</p>
      <p>C: 555.210.4472<span class="sep">|</span> F: 555.210.4472</p>
      <p>tomasreval@morva.com</p>
    </div>
  </section>

  <section class="card card--back" aria-label="Business card back">
    <p class="card__url">WWW.MORVA.COM</p>
  </section>

  <section class="letterhead" aria-label="Letterhead">
    <div class="brand">
      <span class="brand__dot"></span>
      <span class="brand__name">MORVA</span>
    </div>
    <p class="letterhead__affiliation">uma divisão do grupo Draven</p>
    <div class="rule"><span class="rule__violet"></span><span class="rule__amber"></span></div>
    <footer class="letterhead__footer">
      <span>xxxxxxxxx</span><span class="sep">|</span>
      <span class="phone">555-0187</span><span class="sep">|</span>
      <span class="site">www.<b>MORVA</b>.com</span>
    </footer>
  </section>

</body>
</html>
```